Bref créative
Blue Maple Holdings, LLC
Business cards, stationary and envelopes, electronic stationary (Microsoft Word), email signature
Simple
Peter L. Ward
Managing Member
5180 Halvern Court, Suite A
Columbia, MO 65203
pward@bmholdco.example
Phone, email, and name will change for the additional members of the company.
We also want an electronic email signature, and electronic stationary to be used with Microsoft word.
Stationary and envelopes should tie in the theme of the business cards for a uniform look.
Also looking for a Header only version of the stationary, as well as a full page version (header and footer used for design).
Logo used in a creative way.
Horizontal Black Background
Horizontal ALL Black
Horizontal White Background
Horizontal ALL White
Vertical Black Background
Vertical ALL Black
Vertical White Background
Vertical ALL White

```html
<!DOCTYPE html>
<html lang="en">
<head>
<meta charset="utf-8">
<title>Blue Maple Holdings – Stationery Suite</title>
<link href="https://fonts.googleapis.com/css2?family=Russo+One&family=Roboto:wght@400;700&display=swap" rel="stylesheet">
<style>
:root{
  --stage:#3b3b3d;
  --stage-dark:#2c2c2e;
  --brand-red:#c4161c;
  --brand-red-dark:#9a1015;
  --ink:#2b2b2b;
  --paper:#ffffff;
  --paper-shade:#ececec;
  --mark-faint:#e6e6e6;
  --grey-env:#4a4d4f;
}
*{box-sizing:border-box;margin:0;padding:0}
html,body{width:1200px;height:310px;overflow:hidden}
body{background:radial-gradient(ellipse at center,var(--stage) 0%,var(--stage-dark) 100%);font-family:"Roboto",Arial,sans-serif;position:relative}
.piece{position:absolute;background:var(--paper);box-shadow:0 2px 5px rgba(0,0,0,.45);overflow:hidden}
.wordmark{font-family:"Russo One","Arial Black",sans-serif;color:var(--brand-red);text-transform:uppercase;line-height:1;display:flex;align-items:center;gap:6px;white-space:nowrap}
.wordmark .dot{display:inline-block;background:var(--brand-red);flex:none}
.wordmark.on-red{color:var(--paper)}

/* master logo */
.master-logo{position:absolute;left:10px;top:18px;font-size:26px;gap:12px;width:240px}
.master-logo .dot{width:46px;height:46px}
.master-logo span.name{display:block;width:170px;white-space:normal;line-height:1.05}

/* business cards */
.card-front{left:72px;top:165px;width:168px;height:72px;padding:8px}
.card-front .wordmark{font-size:9px}
.card-front .wordmark .dot{width:12px;height:12px}
.card-front .band{position:absolute;left:0;right:0;top:36px;height:9px;background:var(--brand-red)}
.card-front .band span{display:block;font-size:5px;color:#fff;text-align:center;line-height:9px}
.card-front .details{position:absolute;left:8px;bottom:6px;font-size:4px;color:var(--ink);line-height:1.35}
.card-small{top:250px;width:108px;height:54px}
.card-small.white{left:12px}
.card-small.red{left:130px;background:var(--brand-red)}
.card-small .square{position:absolute;left:10px;top:12px;width:26px;height:26px;background:var(--brand-red)}
.card-small.white .wordmark{position:absolute;left:44px;top:22px;font-size:6px}
.card-small.red .wordmark{position:absolute;left:6px;right:6px;top:20px;justify-content:center;font-size:5.5px}
.card-small .rule{position:absolute;left:8px;right:8px;bottom:9px;height:1px;background:#cfcfcf}
.card-small.red .rule{background:rgba(255,255,255,.5)}

/* letterheads */
.letterhead{top:12px;width:216px;height:288px;background:linear-gradient(180deg,var(--paper) 70%,var(--paper-shade))}
.letterhead.one{left:252px}
.letterhead.two{left:480px}
.letterhead .head{position:absolute;left:14px;top:12px;font-size:8px}
.letterhead .head .dot{width:11px;height:11px}
.letterhead .head-info{position:absolute;right:14px;top:11px;font-size:3.6px;color:#666;text-align:right;line-height:1.4}
.letterhead .head-line{position:absolute;left:14px;right:14px;top:32px;height:1px;background:var(--brand-red)}
.letterhead .faint-mark{position:absolute;left:50%;top:128px;width:96px;height:96px;margin-left:-48px;border-radius:50%;background:var(--mark-faint)}
.letterhead .foot{position:absolute;left:0;right:0;bottom:10px;font-size:3.6px;color:#777;text-align:center}
.letterhead .foot-band{position:absolute;left:0;right:0;bottom:0;height:5px;background:linear-gradient(90deg,var(--brand-red),var(--brand-red-dark))}

/* #10 envelopes */
.env-flat{left:708px;width:216px;height:74px}
.env-flat.top{top:108px}
.env-flat.bottom{top:190px}
.env-flat .wordmark{position:absolute;left:10px;top:9px;font-size:7px}
.env-flat .wordmark .dot{width:10px;height:10px}
.env-flat .ret{position:absolute;left:10px;top:23px;font-size:3.4px;color:#777;line-height:1.4}
.env-flat .bar{position:absolute;left:0;right:0;bottom:6px;height:4px;background:var(--brand-red)}
.env-flat .foot{position:absolute;left:0;right:0;bottom:13px;font-size:3.4px;color:#888;text-align:center}

/* envelope backs */
.env-backs{position:absolute;left:948px;top:46px;width:240px;height:232px}
.env-back{position:absolute;left:0;width:240px;height:120px;box-shadow:0 2px 5px rgba(0,0,0,.45)}
.env-back.grey{top:0;background:var(--grey-env)}
.env-back.red{top:50px;background:var(--brand-red)}
.env-back.white{top:110px;background:var(--paper)}
.env-back svg{position:absolute;left:0;top:0}
.env-back .seal{position:absolute;left:112px;width:16px;height:16px}
.env-back.grey .seal{top:22px;background:var(--paper)}
.env-back.white .seal{top:22px;background:var(--brand-red)}
</style>
</head>
<body>

<div class="wordmark master-logo"><i class="dot"></i><span class="name">Blue Maple Holdings</span></div>

<div class="piece card-front">
  <div class="wordmark"><i class="dot"></i>Blue Maple Holdings</div>
  <div class="band"><span>Peter L. Ward · Managing Member</span></div>
  <div class="details">5180 Halvern Court, Suite A · Columbia, MO 65203<br>pward@bmholdco.example</div>
</div>

<div class="piece card-small white">
  <i class="square"></i>
  <div class="wordmark">Blue Maple</div>
  <i class="rule"></i>
</div>
<div class="piece card-small red">
  <div class="wordmark on-red">Blue Maple Holdings</div>
  <i class="rule"></i>
</div>

<div class="piece letterhead one">
  <div class="wordmark head"><i class="dot"></i>Blue Maple Holdings</div>
  <div class="head-info">5180 Halvern Court, Suite A<br>Columbia, MO 65203<br>pward@bmholdco.example</div>
  <i class="head-line"></i>
  <i class="faint-mark"></i>
  <div class="foot">pward@bmholdco.example</div>
</div>

<div class="piece letterhead two">
  <div class="wordmark head"><i class="dot"></i>Blue Maple Holdings</div>
  <i class="faint-mark"></i>
  <div class="foot">5180 Halvern Court, Suite A · Columbia, MO 65203</div>
  <i class="foot-band"></i>
</div>

<div class="piece env-flat top">
  <div class="wordmark"><i class="dot"></i>Blue Maple Holdings</div>
  <div class="ret">5180 Halvern Court, Suite A<br>Columbia, MO 65203</div>
  <i class="bar"></i>
</div>
<div class="piece env-flat bottom">
  <div class="wordmark"><i class="dot"></i>Blue Maple Holdings</div>
  <div class="ret">5180 Halvern Court, Suite A<br>Columbia, MO 65203</div>
  <div class="foot">pward@bmholdco.example</div>
</div>

<div class="env-backs">
  <div class="env-back grey">
    <svg width="240" height="120"><path d="M0 0 L120 62 L240 0" fill="none" stroke="rgba(0,0,0,.35)" stroke-width="1"/></svg>
    <i class="seal"></i>
  </div>
  <div class="env-back red">
    <svg width="240" height="120"><path d="M0 0 L120 62 L240 0" fill="none" stroke="rgba(0,0,0,.3)" stroke-width="1"/></svg>
  </div>
  <div class="env-back white">
    <svg width="240" height="120"><path d="M0 0 L120 62 L240 0" fill="none" stroke="#bbb" stroke-width="1"/><path d="M0 120 L96 64 M240 120 L144 64" stroke="#ddd" stroke-width="1"/></svg>
    <i class="seal"></i>
  </div>
</div>

</body>
</html>
```